Letterhead for Business Law Firm

We need a letter head for our firm based on the design we have settled on and it is attached. Our clients are small and large businesses around the world, and our letterhead is used typically for formal legal purposes such as demand letters (accusing the recipient of doing bad things) or responding to demand letters. It may also be sent to regulators and other government agencies. So this needs to be tasteful, but a little edgy as well - we try to convey that we are a firm that is different - businesses and investors come to us for creative, quick advice, typically in high stress circumstances, and for our ability to work through high conflict situations, and rapid paced engagements.

Target Market(s)

Lawyers, business executives, investors, government regulators who may receive letters from this firm on behalf of its clients.

Industry/Entity Type

Business

Requirements
Must have
• The design and the firm's contact information:
• Thornvale Law Firm, P.C.
• 8172 SW 17th Ave
• Portland, OR 97058
• phone: 971 555 0147
• fax: 971 555 0182
• in what placement and how depicted (e.g. a phone icon instead of the word "phone") I leave to your creative ideas.
Nice to have
• design and information can be placed at the top, bottom and/or sides of the letter, and the design should be for a standard letter size paper - and can have a separate design for the second page.

```html
<!DOCTYPE html>
<html lang="en">
<head>
<meta charset="utf-8">
<title>Thornvale Law Firm, P.C. – Letterhead</title>
<link href="https://fonts.googleapis.com/css2?family=Arimo:wght@400&display=swap" rel="stylesheet">
<style>
  :root {
    --paper: #ffffff;
    --ink-dark: #1f1516;
    --teal: #3d6b7b;
    --teal-deep: #2a4654;
    --band-text: #ffffff;
    --strip-dark: #1b1314;
    --strip-teal: #4d7e8c;
  }
  * { margin: 0; padding: 0; box-sizing: border-box; }
  html, body { width: 848px; height: 1200px; overflow: hidden; background: var(--paper); }
  body { font-family: "Arimo", Arial, sans-serif; }
  .letterhead { position: relative; width: 848px; height: 1200px; background: var(--paper); }

  .firm-name {
    position: absolute; left: 0; width: 848px; top: 1042px;
    text-align: center; font-size: 18px; letter-spacing: 6px;
    color: var(--ink-dark); font-weight: 400; white-space: nowrap;
  }

  .contact-band {
    position: absolute; left: 50px; top: 1074px; width: 746px; height: 52px;
    background: linear-gradient(90deg, var(--teal) 0%, var(--teal-deep) 28%, var(--ink-dark) 55%, var(--ink-dark) 100%);
    color: var(--band-text); font-size: 12px;
  }
  .contact-item {
    position: absolute; top: 0; height: 52px;
    display: flex; flex-direction: column; align-items: center;
  }
  .contact-item .icon { height: 18px; margin-top: 7px; display: flex; align-items: center; justify-content: center; }
  .contact-item .label { margin-top: 7px; white-space: nowrap; line-height: 14px; }
  .sep { display: inline-block; width: 2px; height: 13px; background: var(--band-text); vertical-align: -2px; margin: 0 6px; }

  .address { left: 20px; width: 260px; }
  .web { left: 270px; width: 150px; }
  .phone { left: 432px; width: 186px; }
  .phone .label { font-size: 11px; letter-spacing: 0.5px; }
  .email { left: 628px; width: 116px; }
  .at-sign { font-size: 17px; font-style: italic; line-height: 18px; }

  .pattern-strip {
    position: absolute; left: 50px; top: 1132px; width: 746px; height: 19px;
    background: linear-gradient(90deg, var(--strip-dark) 0%, var(--strip-teal) 12%, var(--strip-dark) 24%, var(--strip-teal) 36%, var(--strip-dark) 48%, var(--strip-teal) 60%, var(--strip-dark) 72%, var(--strip-teal) 84%, var(--strip-dark) 100%);
  }
</style>
</head>
<body>
<main class="letterhead">
  <div class="firm-name">THORNVALE LAW FIRM, P.C.</div>

  <footer class="contact-band">
    <div class="contact-item address">
      <span class="icon">
        <svg width="22" height="15" viewBox="0 0 22 15" aria-hidden="true">
          <rect x="0.75" y="0.75" width="20.5" height="13.5" fill="none" stroke="#fff" stroke-width="1.2"/>
          <polyline points="1,1 11,9 21,1" fill="none" stroke="#fff" stroke-width="1.2"/>
          <polyline points="1,14 8,7" fill="none" stroke="#fff" stroke-width="1"/>
          <polyline points="21,14 14,7" fill="none" stroke="#fff" stroke-width="1"/>
        </svg>
      </span>
      <span class="label">8172 SW 17th Ave<span class="sep"></span>Portland, OR 97058</span>
    </div>

    <div class="contact-item web">
      <span class="icon">
        <svg width="17" height="17" viewBox="0 0 17 17" aria-hidden="true">
          <circle cx="8.5" cy="8.5" r="7.6" fill="none" stroke="#fff" stroke-width="1.2"/>
          <ellipse cx="8.5" cy="8.5" rx="3.4" ry="7.6" fill="none" stroke="#fff" stroke-width="1"/>
          <line x1="1" y1="8.5" x2="16" y2="8.5" stroke="#fff" stroke-width="1"/>
          <line x1="2.2" y1="4.6" x2="14.8" y2="4.6" stroke="#fff" stroke-width="0.9"/>
          <line x1="2.2" y1="12.4" x2="14.8" y2="12.4" stroke="#fff" stroke-width="0.9"/>
        </svg>
      </span>
      <span class="label">www.thornvalelawfirms.com</span>
    </div>

    <div class="contact-item phone">
      <span class="icon">
        <svg width="14" height="17" viewBox="0 0 14 17" aria-hidden="true">
          <rect x="0.6" y="3" width="12.8" height="13.4" fill="none" stroke="#fff" stroke-width="1.2"/>
          <rect x="2" y="0.6" width="3.4" height="13" fill="#fff"/>
          <rect x="7" y="5" width="5" height="3" fill="#fff"/>
          <rect x="7" y="9.5" width="1.6" height="1.4" fill="#fff"/>
          <rect x="10" y="9.5" width="1.6" height="1.4" fill="#fff"/>
          <rect x="7" y="12.3" width="1.6" height="1.4" fill="#fff"/>
          <rect x="10" y="12.3" width="1.6" height="1.4" fill="#fff"/>
        </svg>
      </span>
      <span class="label">T 971 555 0147<span class="sep"></span>F 971 555 0182</span>
    </div>

    <div class="contact-item email">
      <span class="icon at-sign" aria-hidden="true">@</span>
      <span class="label">office@thornvale.com</span>
    </div>
  </footer>

  <div class="pattern-strip" role="img" aria-label="Decorative band of dark panels with teal storm-light accents"></div>
</main>
</body>
</html>
```